organic and vegetable shampoo for dogs

we would like to improve the label of an already existing product which will be part of a range of 5 products. we therefore need labels that are identical but modular in relation to the product.
we have developed a range of vegetable and organic products for dog owners.
We prefer that there are no pictures of dogs, only a drawing or symbol that informs the use of the product on dogs.
It is important to highlight the "vegetable" side;
Free of petro-chemical products, paraben-free, dye-free, synthetic fragrance-free, silicone-free.
we can also accept another typo for the name VERA-MOLUND
The bottle is white and round the height of the label is 115mm and the length 147mm; the visible part is 50mm wide.
there are currently 4 different shampoos:
mild shampoo, shampoo for sensitive skin,
color-enhancing shampoos, anti-hair loss shampoo.
A description in French and in English must be provided.

```html
<!DOCTYPE html>
<html lang="fr">
<head>
<meta charset="utf-8">
<title>Vera-Molund – Shampooing doux</title>
<link rel="stylesheet" href="https://fonts.googleapis.com/css2?family=Dosis:wght@500;600;700;800&display=swap">
<style>
  :root {
    --brand-purple: #5e2a84;
    --water-blue: #0a97d9;
    --sand: #c9b99b;
    --leaf-green: #52a833;
    --frame: #c8c8c8;
    --paper: #ffffff;
  }
  * { margin: 0; padding: 0; box-sizing: border-box; }
  html, body { width: 1200px; height: 1200px; overflow: hidden; background: var(--paper); }
  body { position: relative; font-family: "Dosis", sans-serif; text-transform: uppercase; }

  .label { position: absolute; border: 1px solid var(--frame); background: var(--paper); }
  .label--front { left: 511px; top: 34px; width: 218px; height: 443px; }
  .label--wrap { left: 194px; top: 506px; width: 820px; height: 641px; }

  .abs { position: absolute; }
  .center { left: 0; right: 0; text-align: center; }

  .brand-name { color: var(--brand-purple); font-weight: 800; letter-spacing: 0.04em; }
  .brand-mark { display: block; margin: 0 auto; border-radius: 50%; border: 2px solid var(--brand-purple); }

  .product-title { color: var(--water-blue); font-weight: 700; letter-spacing: 0.01em; }
  .scent-tag {
    display: inline-block; color: var(--sand); font-weight: 600;
    border: 1px solid var(--sand); border-radius: 6px; letter-spacing: 0.02em;
  }
  .volume { color: var(--water-blue); font-weight: 700; }

  .bath-illustration {
    position: absolute; border-radius: 10px;
    background: radial-gradient(circle at 60% 55%, #e4dac7 0%, #efe9dd 55%, #f3f9fd 100%);
  }
  .vegetal-seal { position: absolute; border-radius: 50%; background: var(--leaf-green); border: 2px solid var(--paper); box-shadow: 0 0 0 2px var(--leaf-green); }

  .free-from { color: var(--water-blue); font-weight: 700; font-size: 9px; line-height: 12.2px; letter-spacing: 0.02em; }
  .lang-tag {
    display: inline-block; color: var(--sand); font-weight: 600; font-size: 10px;
    border: 1px solid var(--sand); border-radius: 5px; padding: 1px 7px;
  }
  .description { color: var(--sand); font-weight: 700; font-size: 10.4px; line-height: 14.2px; letter-spacing: 0.02em; }
</style>
</head>
<body>

<!-- Front panel -->
<section class="label label--front">
  <div class="abs center" style="top:18px;">
    <span class="brand-mark" style="width:20px;height:20px;"></span>
  </div>
  <div class="abs center brand-name" style="top:50px;font-size:19px;">VERA-MOLUND</div>

  <div class="abs center product-title" style="top:146px;font-size:19px;">Shampooing doux</div>
  <div class="abs center" style="top:170px;"><span class="scent-tag" style="font-size:10px;padding:1px 8px;">Miel e orange douce</span></div>
  <div class="abs center product-title" style="top:198px;font-size:19px;">Mild shampoo</div>
  <div class="abs center" style="top:222px;"><span class="scent-tag" style="font-size:10px;padding:1px 8px;">Sweet orange and honey</span></div>

  <div class="bath-illustration" style="left:29px;top:266px;width:140px;height:120px;" role="img" aria-label="Line drawing of a dog in a bath tub with bubbles"></div>
  <div class="vegetal-seal" style="left:139px;top:362px;width:34px;height:34px;" role="img" aria-label="100% vegetal seal"></div>

  <div class="abs center volume" style="top:412px;font-size:11px;">200ml</div>
</section>

<!-- Wrap-around label -->
<section class="label label--wrap">
  <div class="abs center" style="top:38px;">
    <span class="brand-mark" style="width:30px;height:30px;"></span>
  </div>
  <div class="abs center brand-name" style="top:74px;font-size:32px;">VERA-MOLUND</div>

  <!-- French column -->
  <div class="abs free-from" style="left:47px;top:198px;">
    0% silicone<br>0% paraben<br>0% parfum de synthèse<br>0% colorant<br>0% de produits issus de la pétrochimie<br>0% conservateur
  </div>
  <div class="vegetal-seal" style="left:47px;top:313px;width:26px;height:26px;" role="img" aria-label="100% vegetal seal"></div>
  <div class="abs" style="left:45px;top:345px;"><span class="lang-tag">French</span></div>
  <p class="abs description" style="left:45px;top:370px;width:180px;">
    Le shampooing Vera-Molund doux,<br>de la marque Halven, est une pro-<br>duit 100% végétal, qui de plus, est<br>fabriqué en Belgique.<br><br>
    Ce shampooing pour chien con-<br>viendra parfaitement à tous les<br>types de poils. Le miel, l'un des<br>composants de ce soin végétal,<br>est connu et reconnu pour ses<br>propriétés hydratantes. Il<br>apporte une douceur et une bril-<br>lance extrême au poil. Tandis<br>qu'un autre de ses composants,<br>l'extrait d'orange douce, purifié<br>l'eau et renforce le poil.
  </p>

  <!-- Centre -->
  <div class="abs center product-title" style="top:214px;font-size:29px;">Shampooing doux</div>
  <div class="abs center" style="top:254px;"><span class="scent-tag" style="font-size:17px;padding:2px 12px;">Miel e orange douce</span></div>
  <div class="abs center product-title" style="top:290px;font-size:29px;">Mild shampoo</div>
  <div class="abs center" style="top:330px;"><span class="scent-tag" style="font-size:17px;padding:2px 12px;">Sweet orange and honey</span></div>

  <div class="bath-illustration" style="left:309px;top:390px;width:216px;height:190px;" role="img" aria-label="Line drawing of a dog in a bath tub with bubbles"></div>
  <div class="vegetal-seal" style="left:464px;top:528px;width:52px;height:52px;" role="img" aria-label="100% vegetal seal"></div>

  <div class="abs center volume" style="top:598px;font-size:15px;">200ml</div>

  <!-- English column -->
  <div class="abs free-from" style="left:610px;top:198px;">
    0% silicone<br>0% paraben<br>0% parfum de synthèse<br>0% colorant<br>0% de produits issus de la pétrochimie<br>0% conservateur
  </div>
  <div class="vegetal-seal" style="left:610px;top:313px;width:26px;height:26px;" role="img" aria-label="100% vegetal seal"></div>
  <div class="abs" style="left:605px;top:347px;"><span class="lang-tag">English</span></div>
  <p class="abs description" style="left:605px;top:374px;width:180px;">
    Le shampooing Vera-Molund doux,<br>de la marque Halven, est une pro-<br>duit 100% végétal, qui de plus, est<br>fabriqué en Belgique.<br><br>
    Ce shampooing pour chien con-<br>viendra parfaitement à tous les<br>types de poils. Le miel, l'un des<br>composants de ce soin végétal,<br>est connu et reconnu pour ses<br>propriétés hydratantes. Il<br>apporte une douceur et une bril-<br>lance extrême au poil. Tandis<br>qu'un autre de ses composants,<br>l'extrait d'orange douce, purifié<br>l'eau et renforce le poil.
  </p>
</section>

</body>
</html>
```